Webdesign fürs Mittagessen
Zielgruppe
Mit unserer Seite kann nach der nächsten Location suchen wo es was zu essen gibt. Das Angebot bezieht sich auf Food Trucks, Imbisse und Restaurants.
Kunden besuchen unsere Seite um dort anhand von Postleitzahlen/Städten nach Orten zu suchen wo es was zu Essen gibt.
Ebenso können Kunden mit guten Locations bei uns Stellplätze für Food Trucks anbieten.
Im angehängten Dokument sind 2 Screenshots der aktuellen Seite. Im Mittelpunkt der Seite steht die Suchfunktion. Das Design aus den Screenshots dient nicht als Orientierung, ebenso wenig wie das angehängt Logo!
Die angehängten Datei bitte ich vertraulich zu behandeln. Sie dürfen in keinster Weise weitergegeben werden oder veröffentlicht werden.
Aufgabenstellung
Das Design sollte übersichtlich und klar gestaltet sein.
Es sollte möglichst wenig knallige Farben haben.
Akzentfarben sind #E9A300 und #0A9DCD.

```html
<!DOCTYPE html>
<html lang="de">
<head>
<meta charset="utf-8">
<title>Mahlzeit Finder – Startseite</title>
<link rel="stylesheet" href="https://fonts.googleapis.com/css2?family=Open+Sans:ital,wght@0,400;0,600;0,700;1,600;1,700&display=swap">
<style>
  :root {
    --accent-orange: #E9A300;
    --accent-blue: #0A9DCD;
    --topbar: #e3d6be;
    --topbar-fade: #efe7d8;
    --text: #555a5e;
    --text-soft: #7c8084;
    --field: #d6d6d6;
    --line: #e2e2e2;
    --card: #ffffff;
    --icon: #9a9ea2;
    --partner: #b9bcbf;
  }
  * { box-sizing: border-box; margin: 0; padding: 0; }
  html, body { width: 1200px; height: 800px; overflow: hidden; }
  body {
    position: relative;
    background: #ffffff;
    font-family: "Open Sans", Arial, sans-serif;
    color: var(--text);
  }
  .topbar {
    position: absolute; left: 0; top: 0; width: 1200px; height: 42px;
    background: linear-gradient(90deg, var(--topbar) 0%, var(--topbar-fade) 50%, var(--topbar) 100%);
    font-size: 8px; color: var(--text-soft);
  }
  .topbar .social-note { position: absolute; left: 312px; top: 17px; display: flex; align-items: center; gap: 5px; }
  .dot { width: 6px; height: 6px; border-radius: 50%; background: var(--text-soft); display: inline-block; }
  .topbar .account { position: absolute; left: 790px; top: 20px; }

  .brand {
    position: absolute; left: 285px; top: 78px; display: flex; align-items: center; gap: 7px;
    font-size: 17px; font-weight: 700; color: var(--accent-blue);
  }
  .brand .mark { width: 14px; height: 14px; border-radius: 50%; background: var(--accent-blue); }

  .search { position: absolute; left: 519px; top: 92px; display: flex; gap: 4px; }
  .select {
    height: 14px; background: var(--field); font-size: 6.5px; color: var(--text-soft);
    padding: 0 5px; display: flex; align-items: center; justify-content: space-between;
  }
  .select::after { content: ""; border: 3px solid transparent; border-top: 4px solid #7a7a7a; margin-top: 3px; margin-left: 4px; }
  .search .btn-search {
    width: 51px; height: 14px; background: var(--accent-orange); color: #fff;
    font-size: 6.5px; display: flex; align-items: center; justify-content: center;
  }
  .advanced { position: absolute; left: 790px; top: 118px; font-size: 6.5px; color: var(--text-soft); }

  .nav {
    position: absolute; left: 285px; top: 147px; width: 580px; height: 22px;
    border-top: 1px solid var(--line); border-bottom: 1px solid var(--line);
    display: flex; justify-content: space-between; align-items: center; padding: 0 14px;
    font-size: 10.5px; color: var(--text);
  }
  .nav a { color: inherit; text-decoration: none; display: flex; align-items: center; gap: 5px; }
  .nav svg { width: 13px; height: 12px; fill: none; stroke: var(--icon); stroke-width: 1.2; }

  .hero {
    position: absolute; left: 0; top: 178px; width: 1200px; height: 450px;
    background:
      radial-gradient(ellipse at 15% 55%, #e6b58a 0%, rgba(230,181,138,0) 45%),
      radial-gradient(ellipse at 88% 60%, #ef9a4b 0%, rgba(239,154,75,0) 35%),
      radial-gradient(ellipse at 78% 35%, #c98c55 0%, rgba(201,140,85,0) 30%),
      radial-gradient(ellipse at 30% 10%, #a7c27a 0%, rgba(167,194,122,0) 35%),
      radial-gradient(ellipse at 95% 90%, #9cc56a 0%, rgba(156,197,106,0) 30%),
      linear-gradient(135deg, #dcc6a4 0%, #eadbc3 50%, #e7c7a0 100%);
  }

  .card { position: absolute; background: var(--card); }
  .card h2 { font-size: 11px; font-weight: 400; color: var(--text); display: flex; align-items: center; gap: 6px; }
  .card h2 svg { width: 11px; height: 11px; fill: var(--icon); }
  .brand-word { color: var(--accent-blue); font-weight: 700; font-style: italic; }
  .small { font-size: 6.5px; line-height: 1.5; color: var(--text); }

  .welcome { left: 288px; top: 198px; width: 354px; height: 152px; padding: 9px 18px; }
  .welcome .lead { font-size: 8.5px; margin: 6px 0 0 1px; }
  .cravings { list-style: none; margin-top: 20px; }
  .cravings li { font-size: 8.5px; color: var(--accent-orange); font-weight: 700; font-style: italic; display: flex; align-items: center; gap: 5px; height: 17px; }
  .cravings li::before { content: ""; width: 9px; height: 8px; border-radius: 2px; background: var(--icon); }
  .bubble {
    position: absolute; border: 1px solid #bfc2c5; border-radius: 50%;
    font-size: 5px; font-style: italic; color: var(--text-soft);
    display: flex; align-items: center; justify-content: center; text-align: center; line-height: 1.3;
  }
  .welcome .intro { position: absolute; left: 18px; top: 117px; width: 320px; }

  .newsletter { left: 653px; top: 198px; width: 211px; height: 152px; padding: 9px 15px; }
  .newsletter .email { margin-top: 22px; height: 17px; background: var(--field); font-size: 7px; color: var(--text-soft); padding: 3px 6px; }
  .newsletter .btn-order { margin-top: 7px; height: 17px; background: var(--accent-orange); color: #fff; font-size: 8.5px; display: flex; align-items: center; justify-content: center; }
  .newsletter .small { margin-top: 18px; padding-left: 2px; }

  .featured { left: 288px; top: 363px; width: 209px; height: 151px; text-align: center; }
  .featured h3 { font-size: 11px; font-weight: 700; font-style: italic; color: var(--accent-blue); margin-top: 11px; }
  .featured .visual { position: absolute; left: 47px; top: 37px; width: 118px; height: 84px; background: linear-gradient(180deg, #a9acaf, #8e9295); border-radius: 8px; }
  .featured .arrow { position: absolute; top: 68px; width: 8px; height: 18px; }
  .featured .arrow svg { stroke: var(--accent-orange); stroke-width: 1.6; fill: none; }
  .featured .caption { position: absolute; left: 20px; top: 126px; width: 169px; font-size: 6.5px; line-height: 1.4; }

  .about { left: 506px; top: 363px; width: 355px; height: 151px; padding: 10px 12px; }
  .about .body { padding: 9px 16px 0; }
  .about .small { margin-bottom: 8px; }

  .partners { left: 288px; top: 527px; width: 573px; height: 70px; padding: 6px 12px; }
  .partner-row { display: flex; justify-content: space-around; align-items: center; margin-top: 10px; padding: 0 20px; }
  .partner-badge { height: 28px; background: var(--partner); border-radius: 3px; }

  .footer { position: absolute; left: 297px; top: 604px; width: 560px; display: flex; justify-content: space-between; font-size: 6px; color: #ffffff; }
  .footer .dots { display: flex; gap: 6px; align-items: center; }
  .footer .dot { background: #f3f3f3; width: 5px; height: 5px; }
</style>
</head>
<body>

<header class="topbar">
  <div class="social-note">Finde uns auf <span class="dot"></span></div>
  <div class="account">Login &nbsp;|&nbsp; Anmelden</div>
</header>

<div class="brand"><span class="mark"></span>Mahlzeit Finder</div>

<form class="search">
  <div class="select" style="width:133px">Dein aktueller Standort</div>
  <div class="select" style="width:48px">Tag</div>
  <div class="select" style="width:139px">Was schmeckt Ihnen ?</div>
  <div class="btn-search">Suchen</div>
</form>
<div class="advanced">Erweiterete Suche</div>

<nav class="nav">
  <a href="#"><svg viewBox="0 0 13 12"><path d="M1 6 L6.5 1 L12 6 M3 5 V11 H10 V5"/></svg>Home</a>
  <a href="#"><svg viewBox="0 0 13 12"><rect x="1" y="2" width="11" height="8" rx="1"/><path d="M1 6 H12"/></svg>FoodTrucks</a>
  <a href="#"><svg viewBox="0 0 13 12"><path d="M2 5 Q6.5 0 11 5 Z M2 7 H11 M2 9 Q6.5 12 11 9"/></svg>Imbisse</a>
  <a href="#"><svg viewBox="0 0 13 12"><path d="M1 10 H12 M2 10 Q6.5 2 11 10 M6.5 3 V2"/></svg>Restaurants</a>
  <a href="#"><svg viewBox="0 0 13 12"><path d="M1 6 L6 1 H12 V7 L7 12 Z"/><circle cx="9.5" cy="3.5" r="1"/></svg>Kosten</a>
  <a href="#"><svg viewBox="0 0 13 12"><circle cx="6.5" cy="3.5" r="2.5"/><path d="M2 12 Q2 6.5 6.5 6.5 Q11 6.5 11 12 Z"/></svg>Über Uns</a>
</nav>

<main class="hero" role="img" aria-label="Foto eines Tellers mit gebratenem Fleisch und buntem Gemüse, unscharf im Hintergrund"></main>

<section class="card welcome">
  <h2><svg viewBox="0 0 11 11"><path d="M5.5 0 A3.8 3.8 0 0 1 9.3 3.8 C9.3 6.5 5.5 11 5.5 11 C5.5 11 1.7 6.5 1.7 3.8 A3.8 3.8 0 0 1 5.5 0 Z"/></svg>Herzlich Willkommen <span class="brand-word">Mahlzeit Finder</span></h2>
  <p class="lead">Wissen Sie schon was es gleich zum Mittag gibt ?</p>
  <ul class="cravings">
    <li>Pizza ?</li>
    <li>Cheesburger ?</li>
    <li>Vegearisches ?</li>
  </ul>
  <div class="bubble" style="left:142px;top:51px;width:56px;height:38px">„Wieder so<br>lange warten.“</div>
  <div class="bubble" style="left:187px;top:82px;width:40px;height:30px">„Wo<br>denn?“</div>
  <div class="bubble" style="left:229px;top:61px;width:54px;height:36px">„Schon wieder<br>das Selbe.“</div>
  <p class="small intro"><span class="brand-word">Mahlzeit Finder</span> kümmert sich Dich. Von uns erfährst Von Uns erfährst du wo die nächste Location ist die dich satt macht. So gibt es endlich mal Abwechslung in deiner Pause.</p>
</section>

<section class="card newsletter">
  <h2><svg viewBox="0 0 11 11"><path d="M0 2 H11 V9 H0 Z" /><path d="M0 2 L5.5 6 L11 2" stroke="#fff" stroke-width="1" fill="none"/></svg>Newsltter empfangen?</h2>
  <div class="email">Ihre E-Mailadresse hier eintragen</div>
  <div class="btn-order">Jetzt bestellen</div>
  <p class="small">Der Newsletter informiert dich über Events rund um das ( mobile) Essen...</p>
</section>

<section class="card featured">
  <h3>Gustav Grün Burger</h3>
  <div class="arrow" style="left:18px"><svg viewBox="0 0 8 18"><path d="M7 1 L1 9 L7 17"/></svg></div>
  <div class="visual" role="img" aria-label="Grafik mit Pommes und Burger"></div>
  <div class="arrow" style="left:184px"><svg viewBox="0 0 8 18"><path d="M1 1 L7 9 L1 17"/></svg></div>
  <p class="caption">„Lecker mit frischen Salat und Hausmannsoße innerhalb von 5 min fertig“</p>
</section>

<section class="card about">
  <h2><svg viewBox="0 0 11 11"><circle cx="5.5" cy="3" r="2.6"/><path d="M1 11 Q1 6 5.5 6 Q10 6 10 11 Z"/></svg>Was ist <span class="brand-word">Mahlzeit Finder?</span></h2>
  <div class="body">
    <p class="small"><span class="brand-word">Mahlzeit Finder</span> beherbergt aktuell 9 Food Trucks/Imbisse/Restaurants über ganz Deutschland verteilt. Insgesamt werden von Ihnen an 8 Standorten Speisen aller Art angeboten.</p>
    <p class="small">Insgesamt wurden auf <span class="brand-word">Mahlzeit Finder</span> bereits 11 Bewertungen und 0 Events eingetragen.</p>
    <p class="small">Das Special für Food Trucks sind unsere aktuell 1 angebotenen Stellplätze.</p>
    <p class="small">Hier kann man neue lukrative Verkaufspunkte finden und direkt mit dem Anbieter in Kontakt treten.</p>
  </div>
</section>

<section class="card partners">
  <h2><svg viewBox="0 0 11 11"><path d="M5.5 0 L7 4 L11 4.2 L7.9 6.7 L9 11 L5.5 8.5 L2 11 L3.1 6.7 L0 4.2 L4 4 Z"/></svg>Unsere Partner</h2>
  <div class="partner-row">
    <div class="partner-badge" style="width:76px"></div>
    <div class="partner-badge" style="width:24px"></div>
    <div class="partner-badge" style="width:118px;height:22px"></div>
    <div class="partner-badge" style="width:66px"></div>
    <div class="partner-badge" style="width:95px"></div>
  </div>
</section>

<footer class="footer">
  <span>Impressum | AGB | Kontakt</span>
  <span class="dots"><span class="dot"></span><span class="dot"></span><span class="dot"></span></span>
</footer>

</body>
</html>
```